Web Design for UK Based Technology Company*

Korvane is a new entrant in the data marketplace.
It is offering two direct API services to help clients access:
- Company Data
- Location Data
We also offer data services and consulting to help companies to integrate our API services and the data derived from them into their businesses. Our aim is to offer both the technology and services to help businesses use and integrate data better. It is a modern business built to support a modern world.

Target Market(s)

Business Professionals and decision makers

Industry/Entity Type

It Service

Number of Pages Required

5+ page

Font styles to use
Sans Serif

Colors

Designer to choose colors to be used in the design.

Requirements
Must have
• The full suite of PSD designs taking into account the layouts and wireframes supplied with which it will be compared. Focus on the homepage first. It has to have a consistent theme/feel. It has to fit with the logo.
Nice to have
• Simple, clean, a few strong ideas.
Should not have
• Cartoons, overdesign, loud colours.

```html
<!DOCTYPE html>
<html lang="en">
<head>
<meta charset="utf-8">
<title>Korvane – Richer data to drive your business</title>
<link rel="stylesheet" href="https://fonts.googleapis.com/css2?family=Lato:wght@400;700;900&display=swap">
<style>
:root{
  --blue:#1d6fb8;
  --blue-bright:#2a7fcb;
  --navy:#0f3d72;
  --deep:#0a2b55;
  --orange:#f7780e;
  --ink:#2f2f2f;
  --grey:#ededee;
  --text:#444;
  --white:#fff;
}
*{box-sizing:border-box;margin:0;padding:0}
html,body{width:1200px;height:4018px;overflow:hidden}
body{position:relative;font-family:'Lato',sans-serif;color:var(--text);background:var(--white)}
.abs{position:absolute}
a{color:inherit;text-decoration:none}
.pill{position:absolute;height:44px;border-radius:22px;display:flex;align-items:center;justify-content:center;gap:8px;font-weight:900;font-size:14px;letter-spacing:.3px;color:var(--white);text-transform:uppercase}
.pill--orange{background:var(--orange)}
.pill--dark{background:var(--ink)}
.pill svg{width:14px;height:14px;fill:currentColor}

/* top bar */
.topbar{position:absolute;left:0;top:0;width:1200px;height:47px;background:var(--blue);color:var(--white);font-size:16px}
.topbar__item{position:absolute;top:12px;display:flex;align-items:center;gap:9px}
.topbar__item svg{width:14px;height:14px;fill:#fff}
.topbar__trial{position:absolute;left:999px;top:0;width:128px;height:47px;background:var(--navy);display:flex;align-items:center;justify-content:center;font-weight:700;font-size:17px}

/* nav */
.brand{position:absolute;left:78px;top:68px;display:flex;align-items:center;gap:14px}
.brand__dot{width:44px;height:44px;border-radius:50%;background:var(--navy)}
.brand__name{font-size:40px;font-weight:700;color:var(--navy);letter-spacing:.5px}
.nav{position:absolute;top:82px;font-size:16px;color:#222}

/* hero */
.hero-title{position:absolute;left:0;top:278px;width:1200px;text-align:center;color:var(--white);font-weight:900;font-size:50px;line-height:50px;text-shadow:0 2px 8px rgba(0,0,0,.35)}
.hero-card{position:absolute;top:418px;width:425px;height:136px;background:rgba(8,26,52,.62);border-radius:12px;color:var(--white);text-align:center;font-weight:900;font-size:24px;line-height:32px;padding-top:24px}

/* intro */
.intro{position:absolute;left:70px;top:800px;width:1060px;text-align:center;font-size:14px;line-height:25px;color:#444}
.intro p{margin-bottom:16px}

/* product sections */
.badge{position:absolute;width:172px;height:172px;border-radius:50%;background:var(--blue);border:4px solid var(--white);box-shadow:0 0 0 3px var(--blue);color:var(--white);text-align:center}
.badge__small{display:block;margin-top:48px;font-size:13px;font-weight:900}
.badge__price{display:block;font-size:58px;font-weight:900;line-height:58px}
.badge__price sup{font-size:30px;vertical-align:22px}
.badge__price small{font-size:28px}
.product-title{position:absolute;font-size:35px;font-weight:900;color:var(--blue)}
.product-text{position:absolute;font-size:22px;line-height:31px;color:#444}

/* cta */
.cta-title{position:absolute;left:0;top:2310px;width:1200px;text-align:center;color:var(--white);font-size:34px;font-weight:900}
.cta-text{position:absolute;left:160px;top:2364px;width:880px;text-align:center;color:var(--white);font-size:22px;line-height:31px}

/* bespoke */
.bespoke-title{position:absolute;left:541px;top:2686px;font-size:34px;line-height:36px;font-weight:900;color:#333}
.bespoke-text{position:absolute;left:541px;font-size:16px;line-height:27px;color:#444}
.ticks{position:absolute;left:541px;top:2856px;list-style:none;font-size:16px;color:#444}
.ticks li{height:32.5px;display:flex;align-items:center;gap:18px}
.ticks svg{width:16px;height:16px}

/* map + card */
.map{position:absolute;left:0;top:3188px;width:1200px;height:470px;
  background:
    radial-gradient(ellipse 200px 140px at 760px 90px,rgba(170,220,140,.55),transparent 70%),
    radial-gradient(ellipse 160px 110px at 980px 20px,rgba(170,220,140,.5),transparent 70%),
    radial-gradient(ellipse 360px 240px at 350px 230px,#f4f4f4,transparent 70%),
    radial-gradient(ellipse 300px 200px at 120px 420px,#dedfe0,transparent 70%),
    linear-gradient(135deg,#ececec,#e4e5e6)}
.locator{position:absolute;left:700px;top:3233px;width:410px;height:332px;background:var(--blue);border-radius:30px;color:var(--white);padding:52px 0 0 48px}
.locator h2{font-size:32px;font-weight:900;margin-bottom:22px}
.locator__row{display:flex;gap:18px;font-size:17px;line-height:28px}
.locator__row svg{width:16px;height:16px;fill:#fff;margin-top:6px;flex:none}

/* footer */
.footer{position:absolute;left:0;top:3650px;width:1200px;height:306px;background:#f3f4f6}
.footer__col{position:absolute;top:85px}
.footer__col h3{font-size:19px;font-weight:900;color:var(--blue);margin-bottom:6px}
.footer__col a{display:block;font-size:14px;line-height:30px;color:#333}
.bottombar{position:absolute;left:0;top:3956px;width:1200px;height:62px;background:var(--blue);color:var(--white);font-size:14px;padding:26px 0 0 75px}
</style>
</head>
<body>

<div class="topbar">
  <a class="topbar__item" style="left:582px">Contact Us</a>
  <span class="topbar__item" style="left:706px"><svg viewBox="0 0 16 16"><path d="M3.6 1l2.3 2.6-1.2 2a9 9 0 0 0 5.4 5.4l2-1.2L14.7 12l-1.6 2.6C6.6 14.6 1.4 9.4 1 2.8z"/></svg>8888 888 888</span>
  <a class="topbar__item" style="left:878px"><svg viewBox="0 0 16 16"><circle cx="8" cy="4.5" r="3.5"/><path d="M1.5 16c0-4 3-6.5 6.5-6.5s6.5 2.5 6.5 6.5z"/></svg>Login</a>
  <a class="topbar__trial">FREE TRIAL</a>
</div>

<div class="brand"><span class="brand__dot"></span><span class="brand__name">KORVANE</span></div>
<a class="nav" style="left:632px">Company Data</a>
<a class="nav" style="left:793px">Location Data</a>
<a class="nav" style="left:946px">Services</a>
<a class="nav" style="left:1058px">About Us</a>

<!-- hero -->
<svg class="abs" style="left:0;top:134px" width="1200" height="620" viewBox="0 0 1200 620" role="img" aria-label="Photograph of a hand touching a glowing blue interface of API and technology icons">
  <defs>
    <linearGradient id="heroBase" x1="0" y1="0" x2="1" y2="1">
      <stop offset="0" stop-color="#1b6fb6"/>
      <stop offset=".55" stop-color="#12559a"/>
      <stop offset="1" stop-color="#0a2f5e"/>
    </linearGradient>
    <radialGradient id="heroGlow1" cx=".5" cy=".5" r=".5">
      <stop offset="0" stop-color="#5fb3f0" stop-opacity=".8"/>
      <stop offset="1" stop-color="#5fb3f0" stop-opacity="0"/>
    </radialGradient>
    <radialGradient id="heroGlow2" cx=".5" cy=".5" r=".5">
      <stop offset="0" stop-color="#3c94de" stop-opacity=".7"/>
      <stop offset="1" stop-color="#3c94de" stop-opacity="0"/>
    </radialGradient>
    <radialGradient id="heroShade" cx=".5" cy=".5" r=".5">
      <stop offset="0" stop-color="#061c3a" stop-opacity=".75"/>
      <stop offset="1" stop-color="#061c3a" stop-opacity="0"/>
    </radialGradient>
    <clipPath id="heroClip"><path d="M0 0H1200V178L1072 586Q1058 618 1000 618L0 538Z"/></clipPath>
  </defs>
  <g clip-path="url(#heroClip)">
    <rect width="1200" height="620" fill="url(#heroBase)"/>
    <ellipse cx="600" cy="260" rx="380" ry="240" fill="url(#heroGlow1)"/>
    <ellipse cx="140" cy="120" rx="260" ry="200" fill="url(#heroGlow2)"/>
    <ellipse cx="1050" cy="150" rx="240" ry="200" fill="url(#heroGlow2)"/>
    <ellipse cx="120" cy="500" rx="320" ry="180" fill="url(#heroShade)"/>
    <ellipse cx="950" cy="520" rx="300" ry="160" fill="url(#heroShade)"/>
  </g>
</svg>
<h1 class="hero-title">RICHER DATA TO DRIVE<br>YOUR BUSINESS</h1>
<div class="hero-card" style="left:164px">COMPREHENSIVE COMPANY<br>INFORMATION</div>
<div class="hero-card" style="left:613px">BRING MAPPING DATA INTO<br>YOUR BUSINESS</div>
<a class="pill pill--orange" style="left:282px;top:531px;width:190px">Company API</a>
<a class="pill pill--orange" style="left:730px;top:531px;width:190px">Location API</a>

<div class="intro">
  <p>Korvane is setup for connected world. A world where data is integrated, comprehensive and useful. Where systems are designed to cooperate to make businesses more efficient. For this purpose we have focused on two key areas of work - location and company data.</p>
  <p>Our Postcode API is the most current in the marketplace, helping anyone pinpoint a map simply by providing a postcode. This allows you to assign a location to your postcode-level business data. We also provide an Address API, giving you an address for any postcode along with it's coordinate on the ground. We also supply base maps for customers looking to use maps on their website. And we supply a wide range of bespoke GIS services for more specific mapping work.</p>
  <p>For company data we have restructured the National Company Register data into something more useful and practical for businesses, Just supply one or more company numbers and we can send you back detailed company information covering a raft of data. Better still this data can be supplied either as a file or by API so you can receive it in the format you prefer.</p>
</div>

<!-- company api -->
<svg class="abs" style="left:0;top:1070px" width="1200" height="640" viewBox="0 0 1200 640">
  <defs>
    <linearGradient id="teamBase" x1="0" y1="0" x2="1" y2="0">
      <stop offset="0" stop-color="#eeeff0" stop-opacity="0"/>
      <stop offset=".3" stop-color="#c9d0d6"/>
      <stop offset=".65" stop-color="#8d98a2"/>
      <stop offset="1" stop-color="#5b6a78"/>
    </linearGradient>
    <radialGradient id="warm" cx=".5" cy=".5" r=".5">
      <stop offset="0" stop-color="#d9a88a" stop-opacity=".75"/>
      <stop offset="1" stop-color="#d9a88a" stop-opacity="0"/>
    </radialGradient>
    <radialGradient id="cool" cx=".5" cy=".5" r=".5">
      <stop offset="0" stop-color="#34495e" stop-opacity=".8"/>
      <stop offset="1" stop-color="#34495e" stop-opacity="0"/>
    </radialGradient>
    <radialGradient id="bright" cx=".5" cy=".5" r=".5">
      <stop offset="0" stop-color="#ffffff" stop-opacity=".9"/>
      <stop offset="1" stop-color="#ffffff" stop-opacity="0"/>
    </radialGradient>
    <clipPath id="teamClip"><path d="M560 100L1200 12V210L1090 580Q1075 620 1030 620L560 585Z"/></clipPath>
  </defs>
  <path d="M0 124L1200 12V540L0 540Z" fill="var(--grey)"/>
  <g clip-path="url(#teamClip)" role="img" aria-label="Photograph of two colleagues working together at a computer with a tablet">
    <rect x="560" y="0" width="640" height="640" fill="url(#teamBase)"/>
    <ellipse cx="650" cy="180" rx="160" ry="120" fill="url(#bright)"/>
    <ellipse cx="770" cy="230" rx="90" ry="110" fill="url(#warm)"/>
    <ellipse cx="900" cy="380" rx="90" ry="100" fill="url(#warm)"/>
    <ellipse cx="880" cy="520" rx="190" ry="110" fill="url(#cool)"/>
    <ellipse cx="1040" cy="340" rx="120" ry="90" fill="url(#cool)"/>
  </g>
  <path d="M0 538L1030 622Q1072 626 1090 582" fill="none" stroke="var(--blue)" stroke-width="9"/>
</svg>
<div class="badge" style="left:949px;top:1131px"><span class="badge__small">FROM ONLY</span><span class="badge__price"><sup>£</sup>29<small>pm</small></span></div>
<h2 class="product-title" style="left:75px;top:1304px">COMPANY API</h2>
<p class="product-text" style="left:76px;top:1354px;width:570px">You supply one or more number we send back everything via a simple &nbsp;API or CSV file.</p>
<a class="pill pill--orange" style="left:75px;top:1451px;width:190px">Find out more</a>
<a class="pill pill--dark" style="left:273px;top:1451px;width:190px">Free Trial</a>

<!-- location api -->
<svg class="abs" style="left:0;top:1640px" width="1200" height="1000" viewBox="0 0 1200 1000">
  <defs>
    <linearGradient id="pinBase" x1="0" y1="0" x2="1" y2="0">
      <stop offset="0" stop-color="#6b7a5c"/>
      <stop offset=".55" stop-color="#b7bcb2"/>
      <stop offset="1" stop-color="#eeeff0" stop-opacity="0"/>
    </linearGradient>
    <radialGradient id="leaf" cx=".5" cy=".5" r=".5">
      <stop offset="0" stop-color="#3f5d34" stop-opacity=".8"/>
      <stop offset="1" stop-color="#3f5d34" stop-opacity="0"/>
    </radialGradient>
    <radialGradient id="card" cx=".5" cy=".5" r=".5">
      <stop offset="0" stop-color="#f2f3ee" stop-opacity=".95"/>
      <stop offset="1" stop-color="#f2f3ee" stop-opacity="0"/>
    </radialGradient>
    <radialGradient id="berry" cx=".5" cy=".5" r=".5">
      <stop offset="0" stop-color="#7a2a3a" stop-opacity=".55"/>
      <stop offset="1" stop-color="#7a2a3a" stop-opacity="0"/>
    </radialGradient>
    <radialGradient id="skin" cx=".5" cy=".5" r=".5">
      <stop offset="0" stop-color="#c98e6a" stop-opacity=".7"/>
      <stop offset="1" stop-color="#c98e6a" stop-opacity="0"/>
    </radialGradient>
    <linearGradient id="ctaFill" x1="0" y1="0" x2="1" y2="1">
      <stop offset="0" stop-color="#0f4a88"/>
      <stop offset="1" stop-color="#1b6bb3"/>
    </linearGradient>
    <clipPath id="pinClip"><path d="M0 0H660V592L115 615Q60 618 40 560L0 470Z"/></clipPath>
  </defs>
  <rect x="0" y="0" width="1200" height="620" fill="var(--grey)"/>
  <g clip-path="url(#pinClip)" role="img" aria-label="Photograph of hands holding a card printed with a map location pin">
    <rect width="660" height="620" fill="url(#pinBase)"/>
    <ellipse cx="120" cy="80" rx="260" ry="170" fill="url(#leaf)"/>
    <ellipse cx="330" cy="310" rx="260" ry="230" fill="url(#card)"/>
    <ellipse cx="350" cy="330" rx="90" ry="110" fill="url(#berry)"/>
    <ellipse cx="70" cy="360" rx="110" ry="90" fill="url(#skin)"/>
    <ellipse cx="560" cy="340" rx="70" ry="60" fill="url(#skin)"/>
  </g>
  <path d="M0 470L40 560Q62 620 120 616L1200 528V990H0Z" fill="url(#ctaFill)"/>
  <path d="M0 470L40 560Q62 620 120 616L1200 528" fill="none" stroke="var(--blue-bright)" stroke-width="9"/>
</svg>
<div class="badge" style="left:79px;top:1763px"><span class="badge__small">FROM ONLY</span><span class="badge__price"><sup>£</sup>29<small>pm</small></span></div>
<h2 class="product-title" style="left:609px;top:1838px">LOCATION API</h2>
<p class="product-text" style="left:610px;top:1888px;width:520px">You send us a postcode we send you the Location. Or you send us the location we send back the postcode: API or CS</p>
<a class="pill pill--orange" style="left:609px;top:2013px;width:190px">Find out more</a>
<a class="pill pill--dark" style="left:807px;top:2013px;width:190px">Free Trial</a>

<h2 class="cta-title">GO AHEAD: TEST OUR DATA; OR LET'S TALK IT THROUGH...</h2>
<p class="cta-text">If you are confident you know what you want, why not start a trial? It's free of charge and you can test the service for a limited time. If you are not so sure or you have a very specific requirements then talk to our consultants,</p>
<a class="pill pill--dark" style="left:406px;top:2493px;width:190px"><svg viewBox="0 0 16 16"><path d="M3.6 1l2.3 2.6-1.2 2a9 9 0 0 0 5.4 5.4l2-1.2L14.7 12l-1.6 2.6C6.6 14.6 1.4 9.4 1 2.8z"/></svg>Call 0000 000 000</a>
<a class="pill pill--orange" style="left:604px;top:2493px;width:190px"><svg viewBox="0 0 16 16"><path d="M1 3h14v1.5L8 9 1 4.5zM1 6.3l7 4.5 7-4.5V13H1z"/></svg>Send an email</a>

<!-- bespoke -->
<div class="abs" style="left:75px;top:2715px;width:440px;height:297px;border-radius:24px;background:radial-gradient(ellipse 180px 120px at 300px 90px,rgba(120,190,245,.7),transparent 70%),radial-gradient(ellipse 200px 140px at 100px 240px,rgba(6,24,60,.8),transparent 70%),linear-gradient(135deg,#0c2f66,#1c6fc0 60%,#4fa0e0)" role="img" aria-label="Abstract blue technology imagery with circuitry and a hand"></div>
<h2 class="bespoke-title">DEMANDING DATA REQUIREMENTS?<br>LOOK NO FURTHER</h2>
<p class="bespoke-text" style="top:2765px;width:570px">Most businesses looking for our help have complex data requirements they need to piece together. It may be they have an in-house team, but if not, we can help with:</p>
<ul class="ticks">
  <li><svg viewBox="0 0 16 16"><circle cx="8" cy="8" r="8" fill="var(--blue)"/><path d="M4.5 8.3l2.3 2.2 4.7-4.8" fill="none" stroke="#fff" stroke-width="1.8"/></svg>Connecting our API into existing systems and software</li>
  <li><svg viewBox="0 0 16 16"><circle cx="8" cy="8" r="8" fill="var(--blue)"/><path d="M4.5 8.3l2.3 2.2 4.7-4.8" fill="none" stroke="#fff" stroke-width="1.8"/></svg>Helping with more complex business or location data supply</li>
  <li><svg viewBox="0 0 16 16"><circle cx="8" cy="8" r="8" fill="var(--blue)"/><path d="M4.5 8.3l2.3 2.2 4.7-4.8" fill="none" stroke="#fff" stroke-width="1.8"/></svg>Placing experienced staff on site to assist with mapping and data projects</li>
  <li><svg viewBox="0 0 16 16"><circle cx="8" cy="8" r="8" fill="var(--blue)"/><path d="M4.5 8.3l2.3 2.2 4.7-4.8" fill="none" stroke="#fff" stroke-width="1.8"/></svg>Helping businesses automate and digitally transform</li>
</ul>
<p class="bespoke-text" style="top:3002px">So if you want us to help you take your integrations up a notch, then let's talk.</p>
<p class="bespoke-text" style="top:3030px;font-weight:700;color:var(--navy)">Please call 0000 000 000 <span style="color:#222">or</span></p>
<a class="pill pill--orange" style="left:543px;top:3078px;width:190px">Bespoke services</a>

<div class="map" role="img" aria-label="Street map showing the area around the Korvane office"></div>
<div class="locator">
  <h2>WHERE IS KORVANE?</h2>
  <div class="locator__row"><svg viewBox="0 0 16 16"><path d="M8 0a5.5 5.5 0 0 0-5.5 5.5C2.5 10 8 16 8 16s5.5-6 5.5-10.5A5.5 5.5 0 0 0 8 0zm0 8a2.5 2.5 0 1 1 0-5 2.5 2.5 0 0 1 0 5z"/></svg><span>Second Floor,12 Larkspur Yard<br>Brindle Park , Ashcombe<br>Eastwick , EW4 2QT.</span></div>
  <div class="locator__row" style="margin-top:4px"><svg viewBox="0 0 16 16"><path d="M3.6 1l2.3 2.6-1.2 2a9 9 0 0 0 5.4 5.4l2-1.2L14.7 12l-1.6 2.6C6.6 14.6 1.4 9.4 1 2.8z"/></svg><span>Contact: 0000 000 000</span></div>
  <a class="pill pill--orange" style="left:49px;top:247px;width:190px">Send an email</a>
</div>

<footer class="footer">
  <div class="footer__col" style="left:75px"><h3>COMPANY DATA</h3><a>Company Information</a><a>Alerts and Notifications</a><a>Contact Information</a><a>Financial Information</a><a>Other Data Services</a></div>
  <div class="footer__col" style="left:360px"><h3>LOCATION DATA</h3><a>Postcode Lookup</a><a>Address Lookup</a><a>Base Mapping</a><a>Boundaries</a><a>Bespoke Mapping</a></div>
  <div class="footer__col" style="left:632px"><h3>SERVICES</h3><a>API / Integrations</a><a>Licensing IPR</a><a>Complex Location</a><a>Data Digital Transformation</a></div>
  <div class="footer__col" style="left:922px"><h3>KORVANE</h3><a>Pricing</a><a>About Us</a><a>Contact Us</a><a>Free Trial</a><a>Login</a></div>
</footer>
<div class="bottombar">Copyright © 2019. Company Name. All rights reserved</div>

</body>
</html>
```